Cardiology practice business card

We need a business card for our cardiology practice "Bellmoor Cardiology". We have a new logo, attached below. We like the colours in the logo - red and charcoal. The front of the business card will need to have the doctors name, address, phone number and email. The back will need to have space to write 2 appointment dates and times.

```html
<!DOCTYPE html>
<html lang="en">
<head>
<meta charset="utf-8">
<title>Bellmoor Cardiology – Business Card</title>
<link href="https://fonts.googleapis.com/css2?family=Fredoka:wght@600&family=Montserrat:wght@400;500;800&display=swap" rel="stylesheet">
<style>
  :root {
    --backdrop: #cccccc;
    --label: #64666a;
    --brand-red: #aa0000;
    --deep-red: #741818;
    --soft-red: #b03333;
    --charcoal: #66676b;
    --charcoal-dark: #606060;
    --charcoal-light: #9a9a9a;
    --mist: #eef1f6;
    --ink: #2b2b2b;
    --white: #ffffff;
  }
  html, body { margin: 0; padding: 0; overflow: hidden; }
  body { width: 1200px; height: 1112px; background: var(--backdrop); }
  .canvas {
    position: relative; width: 1200px; height: 1112px;
    background: var(--backdrop); overflow: hidden;
    font-family: "Montserrat", Arial, sans-serif;
  }
  .side-label {
    position: absolute; margin: 0;
    font-family: "Montserrat", Arial, sans-serif; font-weight: 800;
    font-size: 29px; letter-spacing: 0.5px; color: var(--label); line-height: 1;
  }
  .side-label--front { left: 74px; top: 43px; }
  .side-label--back { left: 371px; top: 562px; }
  .card {
    position: absolute; width: 753px; height: 443px; overflow: hidden;
  }
  .card--front { left: 75px; top: 75px; background: var(--brand-red); }
  .card--back { left: 372px; top: 594px; background: var(--white); }

  .accent-band { position: absolute; top: 0; bottom: 0; }
  .accent-band--front {
    left: 480px; width: 190px;
    background: linear-gradient(180deg, var(--charcoal-dark), var(--charcoal-light));
  }
  .accent-band--front-light {
    left: 690px; width: 24px; background: var(--mist);
  }
  .accent-band--back-main {
    left: 30px; width: 150px;
    background: linear-gradient(180deg, var(--deep-red), var(--soft-red));
  }
  .accent-band--back-side {
    left: 195px; width: 30px; background: var(--charcoal);
  }
  .accent-band--back-edge {
    left: 735px; width: 18px; top: 130px; bottom: 40px;
    background: linear-gradient(90deg, var(--charcoal), var(--soft-red));
  }

  .brand-name {
    position: absolute; left: 78px; top: 172px; margin: 0;
    color: var(--white); font-weight: 500; font-size: 34px; line-height: 1.15;
    text-transform: uppercase; letter-spacing: 3px;
  }
  .brand-name span { display: block; }

  .person-name {
    position: absolute; left: 292px; top: 42px; margin: 0;
    font-family: "Fredoka", Arial, sans-serif; font-weight: 600;
    font-size: 78px; line-height: 1; color: var(--brand-red); white-space: nowrap;
  }
  .person-role {
    position: absolute; left: 293px; top: 142px; margin: 0;
    font-size: 30px; font-weight: 400; color: var(--ink);
  }
  .contact-list {
    position: absolute; left: 293px; top: 279px; margin: 0; padding: 0; list-style: none;
  }
  .contact-list__item {
    display: flex; align-items: center; height: 28px; margin-bottom: 8.5px;
    font-size: 17px; color: var(--ink);
  }
  .contact-list__icon { width: 28px; height: 28px; margin-right: 18px; flex: none; }
</style>
</head>
<body>
<div class="canvas">
  <h2 class="side-label side-label--front">FRONT</h2>
  <section class="card card--front">
    <div class="accent-band accent-band--front" role="img" aria-label="Charcoal decorative band"></div>
    <div class="accent-band accent-band--front-light" role="img" aria-label="Light decorative band"></div>
    <h1 class="brand-name">
      <span>Bellmoor</span>
      <span>Cardiology</span>
    </h1>
  </section>

  <h2 class="side-label side-label--back">BACK</h2>
  <section class="card card--back">
    <div class="accent-band accent-band--back-main" role="img" aria-label="Red decorative band"></div>
    <div class="accent-band accent-band--back-side" role="img" aria-label="Charcoal decorative band"></div>
    <div class="accent-band accent-band--back-edge" role="img" aria-label="Edge decorative band"></div>
    <h1 class="person-name">Your Name</h1>
    <p class="person-role">Cardiology</p>
    <ul class="contact-list">
      <li class="contact-list__item">
        <svg class="contact-list__icon" viewBox="0 0 28 28" aria-hidden="true">
          <circle cx="14" cy="14" r="14" fill="var(--brand-red)"/>
          <path fill="var(--white)" d="M9.5,7.5 L12,7 L13.5,10.5 L12,12 C12.8,13.8 14.2,15.2 16,16 L17.5,14.5 L21,16 L20.5,18.5 C20.2,19.6 19,20.3 17.8,20 C13,18.8 9.2,15 8,10.2 C7.7,9 8.4,7.8 9.5,7.5 Z"/>
        </svg>
        +123-456-7890
      </li>
      <li class="contact-list__item">
        <svg class="contact-list__icon" viewBox="0 0 28 28" aria-hidden="true">
          <circle cx="14" cy="14" r="14" fill="var(--brand-red)"/>
          <rect x="7.5" y="9.5" width="13" height="9" rx="1.5" fill="none" stroke="var(--white)" stroke-width="1.6"/>
          <path d="M8,10.5 L14,15 L20,10.5" fill="none" stroke="var(--white)" stroke-width="1.6"/>
        </svg>
        hello@youremail.com
      </li>
      <li class="contact-list__item">
        <svg class="contact-list__icon" viewBox="0 0 28 28" aria-hidden="true">
          <circle cx="14" cy="14" r="14" fill="var(--brand-red)"/>
          <path fill="var(--white)" d="M14,6.5 C10.9,6.5 8.5,8.9 8.5,11.9 C8.5,15.8 14,21.5 14,21.5 C14,21.5 19.5,15.8 19.5,11.9 C19.5,8.9 17.1,6.5 14,6.5 Z"/>
          <circle cx="14" cy="11.8" r="2.2" fill="var(--brand-red)"/>
        </svg>
        123 Anywhere St., Any City
      </li>
    </ul>
  </section>
</div>
</body>
</html>
```